Dental Business Card

I need Dental oriented business cards.
On the front side -
- on the first line, my name:
Dr Marlow Tasker
- on the second line (just underneath):
Doctor of Dental Medicine
- on the third line, or underneath that or in a corner, I would like the address and phone number:
5192 Ch. Birchfield
Montreal QC H2P 4K8
514-629-5074
- other than that i would maybe like a logo of a tooth, but i want it to be subtle and very basic!
- I would like the card to be preferably black or dark grey-ish with the writing in white
On the other side -
- 2-3 lines with the possibility to write the next appointment the box with the lines should be white, with the rest of the card being black

```html
<!DOCTYPE html>
<html lang="en">
<head>
<meta charset="utf-8">
<title>Dr Marlow Tasker – Business Card</title>
<link href="https://fonts.googleapis.com/css2?family=Lato:wght@400;700&display=swap" rel="stylesheet">
<style>
  :root {
    --stage: #dedede;
    --panel-dark: #1f1f1f;
    --card-light: #f7f5f5;
    --strip: #efefef;
    --ink: #1c1c1c;
    --ink-soft: #2a2a2a;
    --rule: #555555;
  }
  html, body {
    margin: 0;
    width: 1200px;
    height: 900px;
    overflow: hidden;
    background: var(--stage);
    font-family: "Lato", sans-serif;
  }
  .card {
    position: absolute;
    left: 150px;
    top: 170px;
    width: 900px;
    height: 560px;
    background: var(--card-light);
    box-shadow: 0 6px 24px rgba(0,0,0,0.18);
    overflow: hidden;
  }
  .brand-panel {
    position: absolute;
    left: 0;
    top: 0;
    width: 318px;
    height: 424px;
    background: var(--panel-dark);
  }
  .tooth-mark {
    position: absolute;
    left: 38px;
    top: 88px;
    width: 220px;
    height: 300px;
    border-radius: 40% 40% 30% 30%;
    background: radial-gradient(ellipse at center, #3a3a3a 0%, var(--panel-dark) 70%);
  }
  .details {
    position: absolute;
    left: 353px;
    top: 0;
    color: var(--ink);
  }
  .name {
    position: absolute;
    top: 110px;
    margin: 0;
    white-space: nowrap;
    font-size: 43px;
    font-weight: 700;
    letter-spacing: 0.5px;
    text-transform: uppercase;
  }
  .title {
    position: absolute;
    top: 163px;
    margin: 0;
    white-space: nowrap;
    font-size: 27px;
    font-weight: 400;
    color: var(--ink-soft);
  }
  .phone {
    position: absolute;
    top: 236px;
    margin: 0;
    white-space: nowrap;
    display: flex;
    align-items: center;
    gap: 10px;
    font-size: 28px;
    color: var(--ink-soft);
  }
  .phone svg { width: 28px; height: 24px; }
  .address {
    position: absolute;
    top: 308px;
    left: 4px;
    margin: 0;
    white-space: nowrap;
    font-style: normal;
    font-size: 28px;
    line-height: 36px;
    color: var(--ink-soft);
  }
  .appointment-strip {
    position: absolute;
    left: 0;
    top: 424px;
    width: 900px;
    height: 136px;
    background: var(--strip);
  }
  .appointment-label {
    position: absolute;
    left: 29px;
    top: 52px;
    margin: 0;
    font-size: 25px;
    font-weight: 400;
    color: var(--ink);
    text-transform: uppercase;
  }
  .appointment-line {
    position: absolute;
    left: 350px;
    width: 384px;
    height: 0;
    border-top: 1.5px solid var(--rule);
  }
  .appointment-line.first { top: 38px; }
  .appointment-line.second { top: 97px; }
</style>
</head>
<body>
  <div class="card">
    <div class="brand-panel">
      <div class="tooth-mark" role="img" aria-label="Simple white outline of a tooth"></div>
    </div>

    <div class="details">
      <h1 class="name">Dr Marlow Tasker</h1>
      <p class="title">Doctor of Dental Medicine</p>
      <p class="phone">
        <svg viewBox="0 0 28 24" aria-hidden="true">
          <path d="M2 8 Q14 0 26 8 L24 11 L19 9 L19 6 Q14 4 9 6 L9 9 L4 11 Z" fill="#1c1c1c"/>
          <path d="M8 11 L20 11 L24 22 L4 22 Z" fill="#1c1c1c"/>
          <circle cx="14" cy="16" r="2.6" fill="#f7f5f5"/>
        </svg>
        514-629-5074
      </p>
      <address class="address">5192 Ch. Birchfield<br>Montreal QC H2P 4K8</address>
    </div>

    <div class="appointment-strip">
      <p class="appointment-label">Next Appointment</p>
      <div class="appointment-line first"></div>
      <div class="appointment-line second"></div>
    </div>
  </div>
</body>
</html>
```